Letterhead

We are looking for a basic letterhead. It should include our logo, website - northpeakkitchenware.com, phone 907.418.3952, toll free 855.392.6180, and fax 907.418.5263, along with our address 4837 Birchwood Lane, Anchorage, AK 99517. I want something that will look good printed in color or black and white.

```html
<!DOCTYPE html>
<html lang="en">
<head>
<meta charset="utf-8">
<title>North Peak Kitchenware — Letterhead</title>
<link href="https://fonts.googleapis.com/css2?family=Montserrat:wght@700&family=Source+Sans+3:wght@400;700&display=swap" rel="stylesheet">
<style>
  :root {
    --brand-red: #c8404c;
    --brand-red-light: #d35a64;
    --brand-navy: #1f4487;
    --ink: #2b2b2b;
    --paper: #ffffff;
  }
  * { margin: 0; padding: 0; box-sizing: border-box; }
  html, body { width: 971px; height: 1200px; overflow: hidden; background: var(--paper); }
  .letterhead {
    position: relative;
    width: 971px;
    height: 1200px;
    background: var(--paper);
    font-family: "Source Sans 3", "Myriad Pro", Arial, sans-serif;
    color: var(--ink);
  }
  .corner-accent { position: absolute; left: 0; top: 0; }
  .brand-name {
    position: absolute;
    top: 126px;
    left: 0;
    width: 946px;
    text-align: center;
    font-family: "Montserrat", Arial, sans-serif;
    font-weight: 700;
    font-size: 36px;
    letter-spacing: 0.5px;
    color: var(--brand-navy);
  }
  .contact-list {
    position: absolute;
    left: 636px;
    top: 1040px;
    list-style: none;
    font-size: 16px;
    line-height: 1;
  }
  .contact-list li {
    display: flex;
    align-items: center;
    gap: 10px;
    height: 24px;
  }
  .contact-icon { width: 15px; height: 15px; fill: var(--brand-red); flex: none; }
  .toll-free {
    position: absolute;
    left: 636px;
    top: 1141px;
    font-weight: 700;
    font-size: 21px;
    color: var(--brand-red);
  }
  .address {
    position: absolute;
    left: 41px;
    top: 1147px;
    font-size: 14px;
  }
</style>
</head>
<body>
<main class="letterhead">
  <svg class="corner-accent" width="350" height="200" viewBox="0 0 350 200" aria-hidden="true">
    <polygon points="0,0 347,0 157,21 95,141 44,134 0,198" fill="var(--brand-red)"/>
    <polygon points="0,0 347,0 157,21 120,95 0,60" fill="var(--brand-red-light)" opacity="0.35"/>
  </svg>

  <h1 class="brand-name">NORTH PEAK KITCHENWARE</h1>

  <ul class="contact-list">
    <li>
      <svg class="contact-icon" viewBox="0 0 16 16" aria-hidden="true"><rect x="4" y="1" width="8" height="14" rx="1.5"/><rect x="5.5" y="3" width="5" height="6" fill="#fff"/></svg>
      907.418.3952
    </li>
    <li>
      <svg class="contact-icon" viewBox="0 0 16 16" aria-hidden="true"><rect x="4" y="2" width="8" height="5"/><rect x="1" y="7" width="14" height="7" rx="1"/></svg>
      907.418.5263
    </li>
    <li>
      <svg class="contact-icon" viewBox="0 0 16 16" aria-hidden="true"><rect x="1" y="3" width="14" height="10" rx="1"/><path d="M1.5 4 L8 9 L14.5 4" stroke="#fff" stroke-width="1.4" fill="none"/></svg>
      hello@northpeakkitchenware.com
    </li>
    <li>
      <svg class="contact-icon" viewBox="0 0 16 16" aria-hidden="true"><circle cx="8" cy="8" r="6.5" fill="none" stroke="var(--brand-red)" stroke-width="1.5"/><ellipse cx="8" cy="8" rx="2.8" ry="6.5" fill="none" stroke="var(--brand-red)" stroke-width="1.2"/><line x1="1.5" y1="8" x2="14.5" y2="8" stroke="var(--brand-red)" stroke-width="1.2"/></svg>
      northpeakkitchenware.com
    </li>
  </ul>
  <p class="toll-free">toll free 855.392.6180</p>

  <p class="address">address 4837 Birchwood Lane, Anchorage, AK 99517</p>
</main>
</body>
</html>
```